Halvorine.com Web Banner Design

Halvorine.com is a national online business magazine that helps people in Canada start and grow their business. We have over 2000 articles, ask-the-expert answers and guides, as well as a free business directory.

We want to expand awareness for our site and need an exciting, promotional leaderboard and bigbox ad that is highly successful in getting people to click to visit our site, so the ads need to effectively create a sense of urgency. The two ads should share a consistent design and message.

The theme for this first ad group should be that anyone starting a business in Canada should come to Halvorine for the answers they need to succeed. We are looking for creativity and the ads also need to be consistent with the Halvorine brand.
Updates

Reason: Posting on the weekend seems to have limited the number of responses. We do design in house and are outsourcing this project because of time constraints - but we are looking for agency quality work. Check out examples from leading design blogs of great banner ad designs to get a feel for the quality we are looking for. Thank you!

Reason: Liking several of the designs and now just waiting for feedback from some of our advisors!

Reason: Still waiting for input, thank you for your patience. Also, for submissions that have a big box only, we are going to need to have a leaderboard version of the final design.

Target Market(s)

Canadians who or either starting a business or are running their own company with up to 25 staff. Some will be entrepreneurs with plans to grow to be a big company, others will want to make a living and don't want to grow. The common need is that they feel an urgency to get help and to get answers that will let them run their business effectively.

Requirements
Must have
• Halvorine.com name, clearly branded
• Halvorine logo (can be ad the end of the rotation of the ad)
• File size must be 150 kb or smaller
• Leaderboard size: 728 x90 pixels
• Big Box size: 250 x 250 pixels

```html
<!DOCTYPE html>
<html lang="en">
<head>
<meta charset="utf-8">
<title>Halvorine.com Leaderboard</title>
<link rel="stylesheet" href="https://fonts.googleapis.com/css2?family=Arimo:wght@400;700&display=swap">
<style>
  :root {
    --orange-deep: #e85a00;
    --orange-mid: #f7830f;
    --white: #ffffff;
    --brand-navy: #1f3f73;
    --brand-red: #e0261b;
    --button-top: #f4f7fb;
    --button-bottom: #a9b8cc;
    --button-text: #2b3f5c;
    --ribbon-blue: #1f72c4;
    --ribbon-dark: #0f4f94;
  }
  html, body {
    margin: 0;
    padding: 0;
    width: 1200px;
    height: 163px;
    overflow: hidden;
    background: var(--white);
  }
  .leaderboard {
    position: relative;
    width: 1200px;
    height: 163px;
    overflow: hidden;
    background:
      radial-gradient(ellipse 520px 200px at 760px 60px, rgba(255, 200, 110, 0.55), transparent 70%),
      linear-gradient(180deg, var(--orange-mid) 0%, var(--orange-deep) 100%);
    font-family: "Arimo", Arial, sans-serif;
  }
  .light-rays {
    position: absolute;
    inset: 0;
  }
  .brand-panel {
    position: absolute;
    left: 13px;
    top: 14px;
    width: 318px;
    height: 135px;
    background: var(--white);
    border: 2px solid #f3d2b3;
    box-sizing: border-box;
    display: flex;
    align-items: center;
    justify-content: center;
    gap: 12px;
  }
  .brand-mark {
    width: 22px;
    height: 22px;
    background: var(--brand-red);
  }
  .brand-name {
    font-weight: 700;
    font-size: 34px;
    color: var(--brand-navy);
    letter-spacing: 1px;
  }
  .headline {
    position: absolute;
    left: 340px;
    width: 786px;
    top: 18px;
    margin: 0;
    text-align: center;
    color: var(--white);
    font-weight: 700;
    font-size: 35px;
    letter-spacing: 0.5px;
    white-space: nowrap;
    text-shadow: 0 1px 2px rgba(120, 40, 0, 0.5);
  }
  .tagline {
    position: absolute;
    left: 340px;
    width: 786px;
    top: 67px;
    margin: 0;
    text-align: center;
    color: var(--white);
    font-weight: 700;
    font-size: 24px;
    white-space: nowrap;
    text-shadow: 0 1px 2px rgba(120, 40, 0, 0.45);
  }
  .cta-button {
    position: absolute;
    left: 631px;
    top: 102px;
    width: 206px;
    height: 40px;
    border-radius: 5px;
    background: linear-gradient(180deg, var(--button-top) 0%, #d6dfea 50%, var(--button-bottom) 100%);
    border: 1px solid #8a9ab0;
    box-shadow: 0 2px 3px rgba(90, 30, 0, 0.45);
    display: flex;
    align-items: center;
    justify-content: center;
    color: var(--button-text);
    font-weight: 700;
    font-size: 19px;
    text-decoration: none;
    box-sizing: border-box;
  }
  .cta-arrow {
    position: absolute;
    right: 8px;
    bottom: 5px;
  }
  .count-ribbon {
    position: absolute;
    right: 0;
    bottom: 0;
  }
</style>
</head>
<body>
  <div class="leaderboard">
    <svg class="light-rays" width="1200" height="163" viewBox="0 0 1200 163" aria-hidden="true">
      <g fill="#ffd08a" opacity="0.18">
        <polygon points="760,60 520,163 600,163"/>
        <polygon points="760,60 700,163 780,163"/>
        <polygon points="760,60 880,163 960,163"/>
        <polygon points="760,60 1060,163 1140,163"/>
        <polygon points="760,60 1200,40 1200,90"/>
        <polygon points="760,60 1200,-20 1200,5"/>
      </g>
    </svg>

    <div class="brand-panel">
      <span class="brand-mark"></span>
      <span class="brand-name">Halvorine</span>
    </div>

    <h1 class="headline">NATIONAL ONLINE BUSINESS MAGAZINE</h1>
    <p class="tagline">start and grow your business with us!</p>

    <a class="cta-button" href="#">
      CLICK HERE
      <svg class="cta-arrow" width="22" height="22" viewBox="0 0 22 22" aria-hidden="true">
        <rect x="0" y="0" width="22" height="22" rx="3" fill="#f47a10"/>
        <path d="M6 6 L15 15 M15 8 L15 15 L8 15" stroke="#ffffff" stroke-width="2.5" fill="none" stroke-linecap="round" stroke-linejoin="round"/>
      </svg>
    </a>

    <svg class="count-ribbon" width="140" height="140" viewBox="0 0 140 140" aria-label="2000 articles">
      <polygon points="28,140 140,28 140,74 74,140" fill="var(--ribbon-dark)"/>
      <polygon points="32,140 140,32 140,70 70,140" fill="var(--ribbon-blue)"/>
      <text x="0" y="5" transform="translate(95 95) rotate(-45)" text-anchor="middle"
            fill="#ffffff" font-family="Arimo, Arial, sans-serif" font-weight="700" font-size="15">2000 articles</text>
    </svg>
  </div>
</body>
</html>
```